Luxury Face Oil Label

I'm looking for a simple and sophisticated design for a natural face oil that will target the luxe market. It is a pure Natural product. I have attached the logo, Velumi Organics.

Here's the Copy

LUXE FACIAL OIL

Regenerate. Hydrate. Glow

100% Natural

30ml (1.01 oz)

A complex blend of Pure Oils including Marula, Sea Buckthorn, Rosehip, Neroli, Evening primrose, Argan, Calendula, Lavender, Jojoba, Grapeseed, Baobab, Moringa and Vitamin E oil.

Produced by
Amber Reed Ltd
P.O box 7925-00300
Nairobi, Kenya
www.velumiorganics.example

Target Market(s)

High end

Requirements
Must have
• Simple, Please consider the bottle, which is a 30ml clear glass bottle with a gold and white pump. Image attached.
Nice to have
• Very clean designs, not too much going on.
Should not have
• Leaves and nuts.

```html
<!DOCTYPE html>
<html lang="en">
<head>
<meta charset="utf-8">
<title>Velumi Organics – Luxe Facial Oil Label</title>
<link href="https://fonts.googleapis.com/css2?family=Montserrat:wght@400;500;600;700&family=EB+Garamond:wght@400&display=swap" rel="stylesheet">
<style>
  :root {
    --page: #ffffff;
    --olive: #b8b99a;
    --olive-dark: #55574a;
    --ink: #1e1e1e;
    --title: #55574a;
    --frame: #c9c9b8;
    --mono-band: #d4d4d6;
    --mono-dark: #231f20;
    --showcase: #c8c8c8;
    --divider: #000000;
  }
  * { box-sizing: border-box; margin: 0; padding: 0; }
  html, body { width: 1200px; height: 1000px; overflow: hidden; background: var(--page); }
  body { position: relative; font-family: "Montserrat", sans-serif; color: var(--ink); }

  .label {
    --band: var(--olive);
    --accent: var(--olive-dark);
    --heading: var(--title);
    position: absolute;
    width: 744px; height: 373px;
    background: #fff;
    transform-origin: 0 0;
  }
  .label--mono {
    --band: var(--mono-band);
    --accent: var(--mono-dark);
    --heading: var(--ink);
  }
  .label__band {
    position: absolute; left: 0; top: 0; width: 159px; height: 373px;
    background: var(--band);
  }
  .label__maker {
    position: absolute; left: 30px; top: 70px;
    writing-mode: vertical-rl;
    font-size: 15px; line-height: 21.5px; color: var(--ink);
  }
  .label__maker strong { font-weight: 700; }
  .label__volume {
    position: absolute; left: 0; bottom: 0; width: 159px; height: 48px;
    background: var(--accent); color: #fff;
    font-weight: 600; font-size: 19px;
    display: flex; align-items: center; justify-content: center;
  }
  .label__rule { position: absolute; left: 159px; right: 0; height: 12px; background: var(--accent); }
  .label__rule--top { top: 0; }
  .label__rule--bottom { bottom: 0; height: 13px; }

  .brand-mark {
    position: absolute; left: 286px; top: 48px; width: 171px; height: 171px;
    border: 1px solid var(--frame);
    display: flex; align-items: flex-end; justify-content: center;
    padding-bottom: 34px;
  }
  .brand-mark::before {
    content: ""; position: absolute; inset: 4px; border: 1px solid var(--frame);
  }
  .brand-mark__name {
    font-size: 17px; line-height: 22px; font-weight: 400; letter-spacing: 3px; color: var(--heading);
    text-transform: uppercase; text-align: center;
  }

  .product { position: absolute; left: 159px; width: 430px; top: 238px; text-align: center; }
  .product__name { font-size: 26px; font-weight: 600; color: var(--heading); letter-spacing: 0.3px; }
  .product__claims { font-family: "EB Garamond", serif; font-size: 20px; color: var(--heading); margin-top: 2px; }
  .product__natural { font-size: 21px; font-weight: 600; color: var(--heading); margin-top: 2px; }

  .ingredients {
    position: absolute; left: 551px; top: 75px; width: 190px;
    font-size: 15.5px; line-height: 19.6px; color: var(--ink);
  }

  .divider { position: absolute; left: 0; top: 594px; width: 1200px; height: 8px; background: var(--divider); }
  .showcase { position: absolute; left: 0; top: 602px; width: 600px; height: 398px; background: var(--showcase); }

  .front-label {
    position: absolute; left: 256px; top: 805px; width: 92px; height: 140px;
    background: #fff; text-align: center; padding-top: 14px;
    border-top: 4px solid var(--olive-dark); border-bottom: 4px solid var(--olive-dark);
  }
  .front-label__mark {
    width: 44px; height: 44px; margin: 0 auto; border: 1px solid var(--frame);
    display: flex; align-items: flex-end; justify-content: center; padding-bottom: 6px;
    font-size: 5px; line-height: 6px; letter-spacing: 0.8px; color: var(--title); text-transform: uppercase;
  }
  .front-label__name { font-size: 8px; font-weight: 600; color: var(--title); margin-top: 14px; }
  .front-label__claims { font-family: "EB Garamond", serif; font-size: 5.5px; color: var(--title); margin-top: 3px; }
  .front-label__natural { font-size: 6.5px; font-weight: 600; color: var(--title); margin-top: 3px; }
</style>
</head>
<body>

  <section class="label" style="left:228px; top:127px;">
    <div class="label__band">
      <p class="label__maker"><strong>Produced by</strong><br>Amber Reed Ltd<br>P.O box 7925-00300<br>Nairobi, Kenya<br>www.velumiorganics.example</p>
      <div class="label__volume">30ml (1.01 oz)</div>
    </div>
    <div class="label__rule label__rule--top"></div>
    <div class="label__rule label__rule--bottom"></div>
    <div class="brand-mark"><span class="brand-mark__name">Velumi<br>Organics</span></div>
    <div class="product">
      <h1 class="product__name">LUXE FACIAL OIL</h1>
      <p class="product__claims">Regenerate • Hydrate • Glow</p>
      <p class="product__natural">100% Natural</p>
    </div>
    <p class="ingredients">A complex blend<br>of Pure Oils<br>including Marula,<br>Sea Buckthorn,<br>Rosehip, Neroli,<br>Evening primrose,<br>Argan, Calendula,<br>Lavender, Jojoba,<br>Grapeseed,<br>Baobab, Moringa<br>and Vitamin E oil.</p>
  </section>

  <div class="divider"></div>

  <div class="showcase"></div>
  <div class="front-label">
    <div class="front-label__mark">Velumi<br>Organics</div>
    <p class="front-label__name">LUXE FACIAL OIL</p>
    <p class="front-label__claims">Regenerate • Hydrate • Glow</p>
    <p class="front-label__natural">100% Natural</p>
  </div>

  <section class="label label--mono" style="left:645px; top:673px; transform:scale(0.682);">
    <div class="label__band">
      <p class="label__maker"><strong>Produced by</strong><br>Amber Reed Ltd<br>P.O box 7925-00300<br>Nairobi, Kenya<br>www.velumiorganics.example</p>
      <div class="label__volume">30ml (1.01 oz)</div>
    </div>
    <div class="label__rule label__rule--top"></div>
    <div class="label__rule label__rule--bottom"></div>
    <div class="brand-mark"><span class="brand-mark__name">Velumi<br>Organics</span></div>
    <div class="product">
      <h2 class="product__name">LUXE FACIAL OIL</h2>
      <p class="product__claims">Regenerate • Hydrate • Glow</p>
      <p class="product__natural">100% Natural</p>
    </div>
    <p class="ingredients">A complex blend<br>of Pure Oils<br>including Marula,<br>Sea Buckthorn,<br>Rosehip, Neroli,<br>Evening primrose,<br>Argan, Calendula,<br>Lavender, Jojoba,<br>Grapeseed,<br>Baobab, Moringa<br>and Vitamin E oil.</p>
  </section>

</body>
</html>
```